Mediakit / brochure for Dutch Travel Blog

About our company:
• Zwerflust.nl is a Travel- & influence network for independent travellers, outdoor geeks, culture lovers & adventure seekers.
• We don’t sell trips by ourself, we inspire other to travel.
• It’s all about travel inspiration.

About the media kit / brochure:
• The media kit itself must be a travel experience / inspiration.
• Colourful and clean design.
• Use the colours of our new logo
• Use our icons (marker, worldmap) in the design
• Use the style of our website.
• All the text in the media kit must be adjustable by us
• Page format: A4
• Number of pages: 6
• It must be printable as a brochure (for presentations)
• We also need a .pdf version of the brochure (for emailing it to our partners)
• Logo kit added: (1a) + (1b) + (1c) Logo sourcefile

Content of the media kit / brochure
• 6 pages
o (1) Front page
o (2) About Us
o (3) Stats / Companies work with
o (4) Advertising
o (5) Back page
o (6) Our contributors

• Example is attached: (2) example of a brochure with 5 pages A4 (don’t like the design of this example for our media kit, but just to show the idea of the 5 pages).

Maybe use a big travel photo that covers all pages?

For detailed information, I attached the document 'Design brochure Zwerflust (version 2)'.
Updates

Hello designers,Small update for the Cover Page:- Please use one of the images from the attachment I added in the Brief Design: "URL of images for cover.txt"- Use this text "Travel- & influence network for independent travelers, outdoor geeks, culture lovers & adventure seekers."- Add the text MEDIA KIT (remove "2017: )Thanks.Gerbrand Added Thursday, January 5, 2017

Target Market(s)

The mediakit / brochure is for our partners (travel organisations, airline companies, PR companies and big brands like Pine Ridge Gear and Valto).

And the readers of our website are independent travellers, outdoor geeks and adventure seekers. So the theme of the Mediakit must be 'travel inspiration'.

Industry/Entity Type

Travel Industry

Requirements
Must have
• • The media kit itself must be a travel experience / inspiration.
• • Colourful and clean design.
• • Use the colours of our new logo
• • Use our icons (marker, worldmap) in the design
• • Use the style of our website.
• • All the text in the media kit must be adjustable by us
• • Page format: A4
• • Number of pages: 6
• • It must be printable as a brochure (for presentations)
• • We also need a .pdf version of the brochure (for emailing it to our partners)

```html
<!DOCTYPE html>
<html lang="en">
<head>
<meta charset="utf-8">
<title>About Us – Zwerflust</title>
<link rel="stylesheet" href="https://fonts.googleapis.com/css2?family=Montserrat:wght@400;800&display=swap">
<style>
  :root {
    --ink: #2b2b2b;
    --header-band: #363b47;
    --white: #ffffff;
    --accent-pink: #e4237c;
    --accent-cyan: #27b5dc;
    --market-blue: #2f5f8f;
    --market-amber: #c9762c;
    --market-brown: #5a3520;
    --swoosh: #eceef1;
    --map-blue: #bfe3f2;
    --map-yellow: #f3e4a6;
    --map-green: #cfe8c4;
  }
  * { box-sizing: border-box; margin: 0; padding: 0; }
  html, body { width: 848px; height: 1200px; overflow: hidden; background: var(--white); }
  .page {
    position: relative;
    width: 848px;
    height: 1200px;
    overflow: hidden;
    background: var(--white);
    font-family: "Montserrat", Arial, sans-serif;
    color: var(--ink);
  }
  .page-decor { position: absolute; left: 0; top: 0; width: 848px; height: 1200px; }
  .section-header {
    position: absolute;
    left: 114px;
    top: 54px;
    width: 734px;
    height: 71px;
    background: var(--header-band);
  }
  .section-title {
    position: absolute;
    left: 132px;
    top: 62px;
    font-weight: 800;
    font-size: 41px;
    line-height: 56px;
    color: var(--white);
    letter-spacing: 0.5px;
  }
  .header-marker {
    position: absolute;
    left: 48px;
    top: 58px;
    width: 58px;
    height: 58px;
    border-radius: 50%;
    background: var(--header-band);
  }
  .about-copy {
    position: absolute;
    left: 118px;
    top: 168px;
    width: 640px;
    font-size: 16.3px;
    line-height: 22.5px;
  }
  .about-copy p { margin-bottom: 22px; }
  .highlight { color: var(--accent-pink); }
  .site-link { color: var(--accent-cyan); text-decoration: none; }
  .feature-photo {
    position: absolute;
    left: 86px;
    top: 610px;
    width: 677px;
    height: 450px;
    background:
      linear-gradient(180deg, rgba(0,0,0,0) 45%, rgba(90,53,32,0.55) 100%),
      radial-gradient(ellipse at 50% 40%, var(--market-blue) 0%, #1f3c5c 55%, #2a1e14 100%);
    overflow: hidden;
  }
  .feature-photo .jar-row {
    position: absolute;
    left: 0;
    bottom: 40px;
    width: 100%;
    height: 150px;
    background: linear-gradient(90deg, var(--market-brown), var(--market-amber), #d9893a, var(--market-amber), var(--market-brown));
    opacity: 0.85;
  }
  .photo-wedge { position: absolute; left: 0; top: 0; width: 677px; height: 450px; }
</style>
</head>
<body>
<main class="page">
  <svg class="page-decor" viewBox="0 0 848 1200" aria-hidden="true">
    <path d="M0 1010 C 220 930, 520 960, 848 1030 L 848 1200 L 0 1200 Z" fill="var(--swoosh)"/>
    <path d="M0 1080 C 260 1030, 520 1060, 848 1120 L 848 1200 L 0 1200 Z" fill="#f5f6f8"/>
  </svg>
  <svg class="page-decor" viewBox="0 0 848 1200" role="img" aria-label="Faint coloured world map decoration">
    <defs>
      <linearGradient id="mapTone" x1="0" y1="0" x2="1" y2="1">
        <stop offset="0" stop-color="var(--map-blue)"/>
        <stop offset="0.5" stop-color="var(--map-green)"/>
        <stop offset="1" stop-color="var(--map-yellow)"/>
      </linearGradient>
    </defs>
    <path d="M700 900 C 790 880, 848 930, 848 960 L 848 1200 L 640 1200 C 660 1120, 640 1040, 680 980 C 690 950, 680 920, 700 900 Z" fill="url(#mapTone)" opacity="0.55"/>
  </svg>

  <div class="section-header"></div>
  <div class="header-marker"></div>
  <h1 class="section-title">About Us</h1>

  <section class="about-copy">
    <p>Zwerflust is leading in travel inspiration in The Netherlands. Our <span class="highlight">impassioned team</span> of travel journalists, bloggers and youtubers create travel stories about independent &amp; off the beaten track travel, near and afar. Created in 2007, Zwerflust began as a personal backpack blog that has now turned into an <span class="highlight">award winning travel platform.</span></p>
    <p>Our blog is all about providing inspiration for your own journeys no matter how big or small. We love documenting the world around us, seeking out eclectic travel moments and <span class="highlight">inspiring others to live the life they desire.</span> Our knowledge of the world's most inspiring places is unrivalled.</p>
    <p>The travel stories by Zwerflust show us that we can conquer the world, get lost in its beauty, and find ourselves wherever our feet (or passport) may take us. We take our readers and fans on a digital journey around the world in search of the beautiful, the unusual, the forgotten and the mundane. Sit down, relax and have a browse of our inspiring travel stories and videos on <a class="site-link" href="#">www.zwerflust.nl.</a></p>
  </section>

  <div class="feature-photo" role="img" aria-label="Photo of a shopkeeper at a market stall with glass jars of colourful snacks">
    <div class="jar-row"></div>
    <svg class="photo-wedge" viewBox="0 0 677 450" aria-hidden="true">
      <polygon points="0,330 677,245 677,450 0,450" fill="#ffffff" opacity="0.18"/>
    </svg>
  </div>
</main>
</body>
</html>
```